Business Card and Stationary
Cutting Edge Medical Office
Modern
Dr. Paul Drembley
Chiropractor
418 Calder St S
Thief River Falls, MN 56709
NorvaleSpine@example.com
NorvaleSpine.example
I have a cutting edge chiropractic office where we basically do everything different. We use a lot of Bright Path Systems and have a lot of fun in the office. I need my business card and stationary to reflect that.
For Vector File of logo, please download this link:
http://www.filedrop.example/downloads/x9k2m4p7q1r8s3t6v0w5y2z4a7b1c9d3/482263
I for sure do want rounded corners and a double sided business card. I am going to print it on silk so it will look really cool. I would like to make a branding impression and have a swoop with my globe in the upper left on all my stationary designs. On the card it would be great to have a map of where my office is on the back of the card as well as a QR Code as well.
For the actual envelope, there are some restrictions with the design. On the front, there cand really be anything on the bottom half of the envelope. That is because the need that space empty for scanners and whatnot.
Vita Ridge Logo 2D
JPEG file of the Windows
My 3D VR Logo
My 3D VR Logo with Stroke
I am going to be putting a View-Through on all of these windows and doors. I am looking for the same kind of branding to be consistent with my business card as well.

```html
<!DOCTYPE html>
<html lang="en">
<head>
<meta charset="utf-8">
<title>Vita Ridge Family Chiropractic – Stationery</title>
<link rel="stylesheet" href="https://fonts.googleapis.com/css2?family=Open+Sans:wght@400;600;800&display=swap">
<style>
  :root {
    --backdrop: #e9edf1;
    --paper: #ffffff;
    --brand-blue: #1f80d6;
    --brand-blue-deep: #0f5fae;
    --brand-blue-soft: #7fc0ef;
    --brand-green: #5cb531;
    --watermark: #e3f1d9;
    --ink-muted: #6a7a88;
    --shadow: 0 3px 10px rgba(30, 50, 70, 0.18);
  }
  * { box-sizing: border-box; margin: 0; padding: 0; }
  html, body { width: 1200px; height: 518px; overflow: hidden; }
  body {
    background: var(--backdrop);
    font-family: "Open Sans", Arial, sans-serif;
    position: relative;
  }
  .brand { text-align: center; line-height: 1; }
  .brand-name { color: var(--brand-blue); font-weight: 800; letter-spacing: -0.3px; }
  .brand-tagline { color: var(--brand-green); font-weight: 600; }

  /* business cards */
  .card {
    position: absolute; width: 144px; height: 74px;
    background: var(--paper); border-radius: 8px; overflow: hidden;
    box-shadow: var(--shadow);
  }
  .card svg.swoop { position: absolute; left: 0; bottom: 0; width: 144px; height: 40px; }
  .card .brand { position: absolute; top: 10px; left: 0; right: 0; }
  .card .brand-name { font-size: 13px; }
  .card .brand-tagline { font-size: 5px; margin-top: 2px; }
  .card .card-info {
    position: absolute; left: 10px; right: 10px; bottom: 8px;
    color: #fff; font-size: 4.4px; line-height: 1.5;
  }
  .card-back .card-info { bottom: 20px; text-align: center; font-size: 5px; }
  .card-back .brand { top: 6px; }
  .card-a { left: 24px; top: 149px; }
  .card-b { left: 180px; top: 149px; }
  .card-c { left: 24px; top: 252px; }
  .card-d { left: 180px; top: 252px; }

  /* letterhead */
  .letterhead {
    position: absolute; left: 348px; top: 24px; width: 336px; height: 468px;
    background: var(--paper); box-shadow: var(--shadow); overflow: hidden;
  }
  .letterhead .brand { margin-top: 20px; }
  .letterhead .brand-name { font-size: 22px; }
  .letterhead .brand-tagline { font-size: 7px; margin-top: 3px; }
  .watermark { position: absolute; border-radius: 50%; background: var(--watermark); }
  .letterhead .watermark { left: 164px; top: 154px; width: 224px; height: 224px; transform: translateX(-50%); left: 168px; opacity: .8; }
  .letterhead-footer {
    position: absolute; left: 0; right: 0; bottom: 12px; height: 24px;
    background: linear-gradient(180deg, var(--brand-blue-soft), var(--brand-blue));
    color: #fff; font-size: 4.6px; line-height: 1.6; text-align: center; padding-top: 5px;
  }

  /* envelopes */
  .envelope {
    position: absolute; left: 720px; width: 449px; height: 156px;
    background: var(--paper); box-shadow: var(--shadow); overflow: hidden;
  }
  .envelope-back { top: 108px; }
  .envelope-back .flap { position: absolute; inset: 0; }
  .envelope-back .brand { position: absolute; top: 18px; left: 0; right: 0; }
  .envelope-back .brand-name { font-size: 13px; }
  .envelope-back .web { color: var(--brand-blue); font-size: 5px; margin-top: 4px; }
  .envelope-front { top: 307px; }
  .envelope-front .brand { position: absolute; left: 16px; top: 12px; text-align: left; }
  .envelope-front .brand-name { font-size: 14px; }
  .envelope-front .brand-tagline { font-size: 4.5px; margin-top: 2px; }
  .envelope-front .return-address { color: var(--ink-muted); font-size: 4.5px; margin-top: 5px; }
  .envelope-front .watermark { left: 280px; top: 30px; width: 96px; height: 96px; }
</style>
</head>
<body>

  <!-- Business cards -->
  <div class="card card-front card-a">
    <div class="brand"><div class="brand-name">VitaRidge</div><div class="brand-tagline">Family Chiropractic</div></div>
    <svg class="swoop" viewBox="0 0 144 40" preserveAspectRatio="none"><path d="M0 14 Q72 -4 144 12 V40 H0 Z" fill="#7fc0ef"/><path d="M0 20 Q72 4 144 18 V40 H0 Z" fill="#1f80d6"/></svg>
    <div class="card-info">Dr. Paul Drembley · Chiropractor<br>418 Calder St S, Thief River Falls, MN 56709</div>
  </div>
  <div class="card card-front card-b">
    <div class="brand"><div class="brand-name">VitaRidge</div><div class="brand-tagline">Family Chiropractic</div></div>
    <svg class="swoop" viewBox="0 0 144 40" preserveAspectRatio="none"><path d="M0 14 Q72 -4 144 12 V40 H0 Z" fill="#7fc0ef"/><path d="M0 20 Q72 4 144 18 V40 H0 Z" fill="#1f80d6"/></svg>
    <div class="card-info">NorvaleSpine@example.com<br>NorvaleSpine.example</div>
  </div>
  <div class="card card-back card-c">
    <svg class="swoop" viewBox="0 0 144 40" preserveAspectRatio="none"><path d="M0 14 Q72 -4 144 12 V40 H0 Z" fill="#7fc0ef"/><path d="M0 20 Q72 4 144 18 V40 H0 Z" fill="#1f80d6"/></svg>
    <div class="card-info">NorvaleSpine.example</div>
  </div>
  <div class="card card-back card-d">
    <svg class="swoop" viewBox="0 0 144 40" preserveAspectRatio="none"><path d="M0 14 Q72 -4 144 12 V40 H0 Z" fill="#7fc0ef"/><path d="M0 20 Q72 4 144 18 V40 H0 Z" fill="#1f80d6"/></svg>
    <div class="card-info">NorvaleSpine@example.com</div>
  </div>

  <!-- Letterhead -->
  <div class="letterhead">
    <div class="brand"><div class="brand-name">VitaRidge</div><div class="brand-tagline">Family Chiropractic</div></div>
    <div class="watermark" aria-hidden="true"></div>
    <div class="letterhead-footer">
      418 Calder St S · Thief River Falls, MN 56709<br>NorvaleSpine@example.com · NorvaleSpine.example
    </div>
  </div>

  <!-- Envelope back -->
  <div class="envelope envelope-back">
    <svg class="flap" viewBox="0 0 449 156" preserveAspectRatio="none" aria-hidden="true">
      <path d="M0 0 L224 70 L449 0" fill="none" stroke="#dfe5ea" stroke-width="1"/>
    </svg>
    <div class="brand"><div class="brand-name">VitaRidge</div><div class="web">www.NorvaleSpine.example</div></div>
  </div>

  <!-- Envelope front -->
  <div class="envelope envelope-front">
    <div class="brand">
      <div class="brand-name">VitaRidge</div>
      <div class="brand-tagline">Family Chiropractic</div>
      <div class="return-address">418 Calder St S, Thief River Falls, MN 56709</div>
    </div>
    <div class="watermark" aria-hidden="true"></div>
  </div>

</body>
</html>
```